Flyer Design

we need a flyer designing for our independent estate and letting agents based in Gosport Hampshire, our company name is Varley and Partners Gosport, our contact details are 27 Wren Lane, Gosport, Hampshire PO13 4TX, 02392 648307, email :marcia@varleyandpt.example.co.uk. Our special offer we'd like to advertise is for the year 2015 we aim to sell 100 properties and only charge £1000 no vat sellers fee for each property sold. We are also offering a free no obligation market appraisal by one of our professional assessors. The flyer must have this disclaimer added to the bottom of it: if you are currently on the market with another agent then your current terms and conditions may need to be reviewed prior to changing agency. We advertise on Homepanel and would like to see designs that use the colours lime green and navy blue. The final design should be eye catching and promote this special offer.

```html
<!DOCTYPE html>
<html lang="en">
<head>
<meta charset="utf-8">
<title>Varley and Partners – Special Offer Flyer</title>
<link href="https://fonts.googleapis.com/css2?family=Tinos&family=Source+Sans+3:wght@400;500&display=swap" rel="stylesheet">
<style>
  :root{
    --navy:#0b1430;
    --lime:#a9cd38;
    --header-top:#eceef7;
    --header-bottom:#c6cbe3;
    --bar-grey:#a7a9ae;
    --bar-dark:#8d8f94;
    --footer-grey:#8a8b90;
    --page:#ecebe8;
    --white:#ffffff;
    --serif:"Tinos", "Times New Roman", serif;
    --sans:"Source Sans 3", "Myriad Pro", Arial, sans-serif;
  }
  *{box-sizing:border-box;margin:0;padding:0}
  html,body{width:981px;height:1200px;overflow:hidden;background:var(--page)}
  .flyer{position:absolute;left:65px;top:0;width:851px;height:1200px;background:var(--white);font-family:var(--sans)}

  .header{position:absolute;left:0;top:0;width:851px;height:315px;background:linear-gradient(160deg,var(--header-top),var(--header-bottom))}
  .brand{position:absolute;left:62px;top:0;width:330px;height:273px;background:var(--navy);color:var(--white);text-align:center}
  .brand-name{position:absolute;left:0;right:0;top:52px;font-family:var(--serif);font-size:62px;font-weight:400;line-height:1;color:var(--white)}
  .brand-name span{display:block;font-size:40px;margin-top:8px}
  .brand-tagline{position:absolute;left:0;right:0;top:214px;font-family:var(--serif);font-size:15px;letter-spacing:6px;line-height:22px;color:var(--white)}
  .address{position:absolute;left:416px;top:38px;font-size:21px;line-height:29px;color:#2a2d3a}
  .appraisal{position:absolute;left:457px;top:180px;font-size:37px;line-height:48px;color:var(--navy);font-weight:400}

  .photo{position:absolute;left:0;top:320px;width:851px;height:395px;background:linear-gradient(90deg,#6e5a44 0%,#b59a78 30%,#f3f0ea 55%,#ffffff 70%,#3a3a40 100%)}

  .contact-bar{position:absolute;left:0;top:715px;width:851px;height:42px}
  .contact-bar svg.bands{position:absolute;left:0;top:0}
  .contact-item{position:absolute;top:0;height:42px;display:flex;align-items:center;gap:8px;color:var(--white);font-size:16px}
  .contact-item svg{flex:none}

  .offer{position:absolute;left:0;top:757px;width:851px;height:357px;background:var(--navy)}
  .offer-label{position:absolute;left:44px;top:146px;font-family:var(--serif);font-size:36px;font-weight:400;line-height:44px;color:var(--lime);white-space:nowrap}
  .offer-tag{position:absolute;left:314px;top:67px}
  .offer-text{position:absolute;left:337px;top:67px;width:463px;height:198px;text-align:center;font-family:var(--serif);padding-top:22px}
  .offer-text p{font-size:36px;line-height:58px;color:var(--white);white-space:nowrap}
  .offer-text p.fee{font-size:38px;color:var(--navy)}

  .rule{position:absolute;left:0;top:1114px;width:851px;height:4px;background:var(--white)}
  .disclaimer{position:absolute;left:0;top:1118px;width:851px;height:82px;background:var(--footer-grey);color:var(--white);font-size:17.5px;line-height:24px;text-align:center;padding-top:14px}
</style>
</head>
<body>
<main class="flyer">
  <header class="header">
    <div class="brand">
      <div class="brand-name">Varley<span>and Partners</span></div>
      <div class="brand-tagline">ESTATE &amp; LETTING<br>AGENTS</div>
    </div>
    <p class="address">27 Wren Lane, Gosport, Hampshire<br>PO13 4TX</p>
    <h1 class="appraisal">Free No Obligation<br>Market Appraisal!</h1>
  </header>

  <div class="photo" role="img" aria-label="Photo: a smiling couple receiving house keys from an estate agent holding documents in a bright room"></div>

  <div class="contact-bar">
    <svg class="bands" width="851" height="42" viewBox="0 0 851 42">
      <polygon points="0,0 312,0 298,42 0,42" fill="var(--bar-grey)"/>
      <polygon points="312,0 600,0 586,42 298,42" fill="var(--bar-dark)"/>
      <polygon points="600,0 851,0 851,42 586,42" fill="var(--lime)"/>
    </svg>
    <div class="contact-item" style="left:28px">
      <svg width="16" height="13" viewBox="0 0 16 13"><path d="M1 5 L8 1 L15 5 V12 H1 Z M1 5 L8 9 L15 5" fill="none" stroke="#fff" stroke-width="1.5"/></svg>
      marcia@varleyandpt.example.co.uk
    </div>
    <div class="contact-item" style="left:326px">
      <svg width="16" height="16" viewBox="0 0 16 16" fill="none" stroke="#fff" stroke-width="1.3"><circle cx="8" cy="8" r="7"/><ellipse cx="8" cy="8" rx="3" ry="7"/><path d="M1 8 H15 M2.5 4.5 H13.5 M2.5 11.5 H13.5"/></svg>
      www.varleyandpt.example.co.uk
    </div>
    <div class="contact-item" style="left:634px;font-size:18px">
      <svg width="22" height="16" viewBox="0 0 22 16"><path d="M1 6 Q11 -2 21 6 L18 8 L15 5 H7 L4 8 Z" fill="#fff"/><path d="M6 7 H16 L19 15 H3 Z" fill="#fff"/><circle cx="11" cy="11" r="2.2" fill="var(--lime)"/></svg>
      02392 648307
    </div>
  </div>

  <section class="offer">
    <h2 class="offer-label">SPECIAL OFFER</h2>
    <svg class="offer-tag" width="490" height="198" viewBox="0 0 490 198">
      <polygon points="23,0 486,0 486,198 23,198 23,110 0,99 23,88" fill="var(--lime)"/>
      <polygon points="29,5 480,5 480,193 29,193 29,114 8,99 29,84" fill="none" stroke="var(--navy)" stroke-width="1" stroke-dasharray="2 2"/>
    </svg>
    <div class="offer-text">
      <p>For The Year 2015</p>
      <p>100 Properties With</p>
      <p class="fee">£1000 NO VAT sellers fee!</p>
    </div>
  </section>

  <div class="rule"></div>
  <p class="disclaimer">If you are currently on the market with another agent then your current terms and conditions<br>may need to be reviewed prior to changing agency</p>
</main>
</body>
</html>
```